Marlow Creek sign

24"x36" sign for new home construction job site. Located in affluent in-town neighborhood in Midwest. Traditional american style homes. 2nd generation construction company. Sign needs to convey strength and elegance but not overly elaborate. Competition most has signs consisting of text.

Sign text reads:
Marlow Creek Builders
Custom Luxury for Over 20 years
248-555-0137

Target Market(s)

Upper middle income home buyers

Industry/Entity Type

Construction

Font styles to use
Serif
Decorative

Requirements
Must have
• Logo image no more than 2 colors
Nice to have
• Should be visible and legible from distance of 30'
Should not have
• Not just image of house as logo

```html
<!DOCTYPE html>
<html lang="en">
<head>
<meta charset="utf-8">
<title>Marlow Creek Builders – Job Site Sign</title>
<link rel="stylesheet" href="https://fonts.googleapis.com/css2?family=Archivo:wdth,wght@125,900&family=Open+Sans:wght@400&display=swap">
<style>
  :root {
    --backdrop: #4a4a4b;
    --sign-light: #f3f4f5;
    --sign-edge: #e4e5e7;
    --brand-blue: #0e548c;
    --steel-grey: #6b6e71;
    --ink: #111111;
  }
  html, body {
    margin: 0;
    padding: 0;
    width: 1200px;
    height: 999px;
    overflow: hidden;
    background: var(--backdrop);
  }
  .sign {
    position: absolute;
    left: 289px;
    top: 43px;
    width: 622px;
    height: 932px;
    overflow: hidden;
    background: radial-gradient(ellipse at 50% 55%, var(--sign-light) 40%, var(--sign-edge) 100%);
  }
  .sign-swooshes {
    position: absolute;
    inset: 0;
    width: 622px;
    height: 932px;
  }
  .company-name {
    position: absolute;
    left: 0;
    top: 144px;
    width: 100%;
    margin: 0;
    text-align: center;
    font-family: "Archivo", "Arial Black", sans-serif;
    font-stretch: 125%;
    font-weight: 900;
    font-size: 74px;
    line-height: 100px;
    color: var(--brand-blue);
    letter-spacing: 1px;
  }
  .company-name span {
    display: block;
    transform: scaleX(1.23);
    transform-origin: 50% 50%;
  }
  .tagline {
    position: absolute;
    left: 0;
    top: 456px;
    width: 100%;
    margin: 0;
    text-align: center;
    font-family: "Open Sans", "Myriad Pro", sans-serif;
    font-size: 50px;
    line-height: 66px;
    color: var(--ink);
  }
  .phone {
    position: absolute;
    left: 0;
    top: 824px;
    width: 100%;
    margin: 0;
    text-align: center;
    font-family: "Archivo", "Arial Black", sans-serif;
    font-stretch: 125%;
    font-weight: 900;
    font-size: 58px;
    line-height: 70px;
    color: var(--brand-blue);
    letter-spacing: 1px;
    transform: scaleX(1.26);
    transform-origin: 50% 50%;
  }
</style>
</head>
<body>
  <div class="sign">
    <svg class="sign-swooshes" viewBox="0 0 622 932" aria-hidden="true">
      <path class="swoosh-top-blue" d="M348,0 Q470,110 622,175 L622,0 Z" fill="var(--brand-blue)"/>
      <path class="swoosh-top-grey" d="M372,0 Q490,98 622,152 L622,0 Z" fill="var(--steel-grey)"/>
      <path class="swoosh-bottom-grey" d="M0,607 Q250,772 622,778 L622,810 Q250,802 0,648 Z" fill="var(--steel-grey)"/>
      <path class="swoosh-bottom-blue" d="M0,512 Q250,690 622,702 L622,772 Q250,768 0,607 Z" fill="var(--brand-blue)"/>
    </svg>
    <h1 class="company-name"><span>MARLOW</span><span>CREEK</span><span>BUILDERS</span></h1>
    <p class="tagline">Custom Luxury for<br>Over 20 years</p>
    <p class="phone">248-555-0137</p>
  </div>
</body>
</html>
```